HearthBay business card and stationary design

We are looking for a simple yet elegant design for our mortgage company business card and stationary.

The card should include:
Name (Doug Warley)
Title (CEO)
Phone Number (614-382-9047)
Address (48 Birchwood Terrace, Suite 315, Marlow, NJ 08214)
Email (email@hearthbay.example)
"NMLS" i.e. (NMLS 61947)
"Company NMLS" (Company NMLS 492716)

Contact Information for Business Card

See above

```html
<!DOCTYPE html>
<html lang="en">
<head>
<meta charset="UTF-8">
<title>HearthBay Business Card</title>
<link href="https://fonts.googleapis.com/css2?family=Montserrat:wght@400;500;600;700&display=swap" rel="stylesheet">
<style>
  :root {
    --page-bg: #2b2d31;
    --navy: #1b2531;
    --blue: #1fa3e1;
    --white: #ffffff;
    --ink: #2f3338;
  }
  * { box-sizing: border-box; margin: 0; padding: 0; }
  html, body {
    width: 1200px;
    height: 900px;
    overflow: hidden;
    background: var(--page-bg);
    font-family: "Montserrat", sans-serif;
  }
  .canvas {
    width: 1200px;
    height: 900px;
    display: flex;
    flex-direction: column;
    align-items: center;
    justify-content: center;
    gap: 40px;
  }
  .card {
    width: 700px;
    height: 400px;
    position: relative;
    box-shadow: 0 12px 30px rgba(0,0,0,0.35);
  }

  /* Front */
  .card-front {
    background: var(--white);
    display: flex;
    align-items: center;
  }
  .front-brand {
    width: 330px;
    padding-left: 50px;
    font-size: 46px;
    font-weight: 600;
    color: var(--navy);
    letter-spacing: 0.5px;
  }
  .divider {
    width: 2px;
    height: 230px;
    background: var(--blue);
  }
  .contact {
    padding-left: 34px;
    color: var(--ink);
    font-size: 17px;
    line-height: 1.4;
  }
  .contact-name {
    color: var(--blue);
    font-weight: 700;
    font-size: 24px;
    letter-spacing: 1px;
    text-transform: uppercase;
  }
  .contact-title { margin-bottom: 10px; }
  .contact-address { margin-bottom: 10px; }
  .contact-line {
    display: flex;
    align-items: center;
    gap: 10px;
  }
  .contact-line svg { width: 15px; height: 15px; flex: none; }

  /* Back */
  .card-back {
    background: var(--navy);
    display: flex;
    flex-direction: column;
    align-items: center;
    justify-content: center;
    gap: 34px;
  }
  .back-brand {
    font-size: 74px;
    font-weight: 600;
    color: var(--white);
    letter-spacing: 1px;
  }
  .licenses {
    color: var(--white);
    font-size: 17px;
    letter-spacing: 1px;
    display: flex;
    align-items: center;
    gap: 14px;
  }
  .licenses .dot {
    width: 7px;
    height: 7px;
    border-radius: 50%;
    background: var(--blue);
  }
</style>
</head>
<body>
<main class="canvas">
  <section class="card card-front">
    <div class="front-brand">HearthBay</div>
    <div class="divider"></div>
    <div class="contact">
      <div class="contact-name">Doug Warley</div>
      <div class="contact-title">CEO</div>
      <div class="contact-address">48 Birchwood Terrace, Suite 315<br>Marlow, NJ 08214</div>
      <div class="contact-line">
        <svg viewBox="0 0 16 16" aria-hidden="true"><path fill="#1fa3e1" d="M3.6 1.5l2.3 2.6-1.3 1.7c.9 2 2.4 3.6 4.5 4.6l1.7-1.3 2.7 2.3-1.3 2.4C7 13.4 2.6 9 1.3 2.8z"/></svg>
        <span>614-382-9047</span>
      </div>
      <div class="contact-line">
        <svg viewBox="0 0 16 16" aria-hidden="true"><rect x="1" y="3" width="14" height="10" fill="#1fa3e1"/><path d="M1 3.5l7 5 7-5" stroke="#fff" stroke-width="1.3" fill="none"/></svg>
        <span>email@hearthbay.example</span>
      </div>
      <div class="contact-line">
        <svg viewBox="0 0 16 16" aria-hidden="true"><circle cx="8" cy="8" r="6.5" fill="none" stroke="#1fa3e1" stroke-width="1.6"/><path d="M1.5 8h13M8 1.5c-3 3.5-3 9.5 0 13M8 1.5c3 3.5 3 9.5 0 13" fill="none" stroke="#1fa3e1" stroke-width="1.2"/></svg>
        <span>www.hearthbay.example</span>
      </div>
    </div>
  </section>

  <section class="card card-back">
    <div class="back-brand">HearthBay</div>
    <div class="licenses">
      <span>NMLS 61947</span>
      <span class="dot"></span>
      <span>Company NMLS 492716</span>
    </div>
  </section>
</main>
</body>
</html>
```